Fire Hydrant Repair Parts Flyer

We need a flyer advertising both fire hydrant parts and the manufacturers that we are stocking. Our company is Coastal Flowline Supply and we are a parts distributor who sells directly to contractors. I have attached an example flyer that advertises some other parts we stock. We don't want it to look exactly like the old flyer, but we would like it to be structured similarly. I have also attached a background image for the flyer as well as some pictures of the parts we are stocking. I have also attached pictures of the manufacturer logos that we are stocking. We are trying to convey the parts that we are stocking which are: "Traffic Repair Kits", "Main Valve Repair Kits", "Extension Kits", "Replacement Caps & Gaskets", "Replacement Nozzles", Adjustable Hydrant Wrenches", "Hydrant Diffusers", & "Hydrant Oil". I have attached pictures of some of these items that we would like placed on the flyer. Let me know if you have any questions at all.

```html
<!DOCTYPE html>
<html lang="en">
<head>
<meta charset="utf-8">
<title>Fire Hydrant Repair Parts – Coastal Flowline Supply</title>
<link rel="stylesheet" href="https://fonts.googleapis.com/css2?family=Poppins:wght@400;500;600;700;800&display=swap">
<style>
  :root {
    --navy: #1b2a7a;
    --navy-dark: #142063;
    --red: #c8102e;
    --red-dark: #a90d27;
    --paper: #f5f6f8;
    --ink: #333844;
    --white: #ffffff;
    --stage: #e7e8ea;
  }
  * { margin: 0; padding: 0; box-sizing: border-box; }
  html, body { width: 1200px; height: 2982px; overflow: hidden; }
  body { background: var(--stage); font-family: "Poppins", sans-serif; position: relative; }

  .flyer {
    position: absolute; left: 0; top: 714px;
    width: 1200px; height: 1553px;
    background: radial-gradient(circle at 85% 45%, #ffffff 0%, var(--paper) 60%, #eceef2 100%);
    overflow: hidden;
  }
  .flyer-shapes { position: absolute; inset: 0; }

  .brand { position: absolute; left: 70px; top: 82px; display: flex; align-items: center; gap: 16px; }
  .brand-dot { width: 40px; height: 40px; border-radius: 50%; background: var(--red); }
  .brand-name { font-size: 38px; font-weight: 400; color: var(--navy); letter-spacing: -0.5px; }

  .headline { position: absolute; left: 72px; top: 200px; color: var(--white); line-height: 0.98; }
  .headline .big { display: block; font-size: 80px; font-weight: 800; letter-spacing: 1px; }
  .headline .sub { display: block; font-size: 52px; font-weight: 800; margin-top: 10px; letter-spacing: 0.5px; }

  .about { position: absolute; left: 70px; top: 520px; width: 1060px; }
  .about-title { font-size: 32px; font-weight: 400; color: var(--ink); letter-spacing: 0.5px; }
  .about-title b { font-weight: 700; color: var(--navy); }
  .about-text {
    margin-top: 10px; border-left: 4px solid var(--red); padding-left: 18px;
    font-size: 16px; line-height: 1.4; color: var(--ink);
  }

  .products-title {
    position: absolute; left: 371px; top: 641px; width: 504px; height: 62px;
    display: flex; align-items: center; justify-content: center;
    color: var(--white); font-size: 32px; font-weight: 400; letter-spacing: 0.5px;
  }
  .products-title b { font-weight: 700; margin-left: 8px; }
  .product-list { position: absolute; top: 748px; list-style: none; }
  .product-list li {
    height: 57px; display: flex; align-items: center; gap: 18px;
    color: var(--white); font-size: 26px; font-weight: 600; white-space: nowrap;
  }
  .product-list.left { left: 88px; }
  .product-list.right { left: 636px; }
  .product-list svg { width: 36px; height: 22px; flex: none; }

  .cards { position: absolute; left: 66px; top: 1071px; display: flex; gap: 13px; }
  .card { width: 168px; height: 217px; background: var(--white); border: 2px solid #c9ccd4; display: flex; flex-direction: column; }
  .card-image { flex: 1; margin: 10px; border-radius: 4px; }
  .card-label {
    height: 62px; background: var(--navy); color: var(--white);
    font-size: 17px; font-weight: 600; line-height: 1.2; text-align: center;
    display: flex; align-items: center; justify-content: center; padding: 0 6px;
  }
  .img-traffic { background: radial-gradient(circle, #8a8d93 0%, #3b3e44 55%, #ffffff 80%); }
  .img-extension { background: radial-gradient(circle, #7d7f83 0%, #2f3033 50%, #ffffff 78%); }
  .img-cap { background: radial-gradient(circle at 50% 35%, #d62a3c 0%, #b7bcc3 45%, #ffffff 78%); }
  .img-diffuser { background: radial-gradient(circle at 40% 40%, #f2b400 0%, #c7c9cc 50%, #ffffff 78%); }
  .img-wrench { background: linear-gradient(135deg, #ffffff 20%, #b8bcc2 50%, #ffffff 80%); }
  .img-oil { background: radial-gradient(ellipse 30% 60% at 50% 50%, #eceef0 0%, #c4c7cc 60%, #ffffff 100%); }

  .makers { position: absolute; left: 66px; top: 1331px; display: flex; gap: 13px; }
  .maker { width: 168px; height: 65px; background: #e4e6ea; display: flex; align-items: center; justify-content: center; }
  .maker-mark { width: 56px; height: 36px; background: #b9bdc5; border-radius: 4px; }
  .maker-mark.round { width: 38px; height: 38px; border-radius: 50%; }

  .contact-call {
    position: absolute; left: 70px; top: 1458px; height: 95px;
    display: flex; align-items: center; gap: 12px; color: var(--white); white-space: nowrap;
  }
  .contact-call .label { font-size: 25px; font-weight: 600; }
  .contact-call .number { font-size: 38px; font-weight: 500; letter-spacing: 0.5px; }
  .contact-web {
    position: absolute; left: 790px; top: 1458px; height: 95px;
    display: flex; align-items: center; gap: 12px; color: var(--white);
    font-size: 30px; font-weight: 600; white-space: nowrap;
  }
  .contact-call svg, .contact-web svg { flex: none; }
</style>
</head>
<body>
<main class="flyer">
  <svg class="flyer-shapes" width="1200" height="1553" viewBox="0 0 1200 1553">
    <defs>
      <linearGradient id="photoTone" x1="0" y1="0" x2="1" y2="1">
        <stop offset="0" stop-color="#6f8f4a"/>
        <stop offset="0.35" stop-color="#8b9196"/>
        <stop offset="0.55" stop-color="#b8202c"/>
        <stop offset="0.75" stop-color="#dfe4e8"/>
        <stop offset="1" stop-color="#f2f4f6"/>
      </linearGradient>
    </defs>
    <polygon role="img" aria-label="Photo of a red fire hydrant on grass, flushing a jet of water" points="720,0 1200,0 1200,510 650,510 535,330" fill="url(#photoTone)"/>
    <polyline points="694,0 506,330 620,510" fill="none" stroke="var(--white)" stroke-width="10"/>
    <polyline points="672,0 486,330 600,510" fill="none" stroke="var(--navy)" stroke-width="8"/>
    <polyline points="650,0 464,330" fill="none" stroke="var(--red)" stroke-width="7"/>
    <polygon points="0,175 470,175 530,320 470,460 0,460" fill="var(--navy)"/>
    <polygon points="480,175 500,175 560,320 500,460 480,460 540,320" fill="var(--red)"/>
    <polygon points="440,460 545,460 575,505 470,505" fill="var(--red)"/>
    <rect x="604" y="510" width="596" height="12" fill="var(--red)"/>
    <polygon points="100,641 1130,641 1130,980 1100,1009 66,1009 66,675" fill="var(--red)"/>
    <polygon points="371,641 875,641 850,703 396,703" fill="var(--navy)"/>
    <line x1="584" y1="760" x2="584" y2="978" stroke="var(--white)" stroke-width="2" stroke-dasharray="6 6" opacity="0.8"/>
    <line x1="1088" y1="1040" x2="1135" y2="994" stroke="var(--navy)" stroke-width="5"/>
    <polygon points="0,1458 700,1458 730,1553 0,1553" fill="var(--red)"/>
    <polygon points="715,1458 1200,1458 1200,1553 745,1553" fill="var(--white)"/>
    <polygon points="730,1458 1200,1458 1200,1553 760,1553" fill="var(--navy)"/>
  </svg>

  <div class="brand">
    <span class="brand-dot"></span>
    <span class="brand-name">Coastal Flowline Supply</span>
  </div>

  <h1 class="headline">
    <span class="big">FIRE</span>
    <span class="big">HYDRANT</span>
    <span class="sub">REPAIR PARTS</span>
  </h1>

  <section class="about">
    <h2 class="about-title">ABOUT <b>US</b></h2>
    <p class="about-text">Coastal Flowline Supply has a full service Gauge Repair Department. We can repair anything on your test kit<br>from hose replacement to full internal cleaning and we service all manufacturers and models.</p>
  </section>

  <h2 class="products-title">OUR <b>PRODUCTS</b></h2>
  <ul class="product-list left">
    <li><svg viewBox="0 0 36 22"><polyline points="4,4 14,11 4,18" fill="none" stroke="#fff" stroke-width="3"/><polyline points="16,4 26,11 16,18" fill="none" stroke="#fff" stroke-width="3"/></svg>Traffic Repair Kits</li>
    <li><svg viewBox="0 0 36 22"><polyline points="4,4 14,11 4,18" fill="none" stroke="#fff" stroke-width="3"/><polyline points="16,4 26,11 16,18" fill="none" stroke="#fff" stroke-width="3"/></svg>Main Valve Repair Kits</li>
    <li><svg viewBox="0 0 36 22"><polyline points="4,4 14,11 4,18" fill="none" stroke="#fff" stroke-width="3"/><polyline points="16,4 26,11 16,18" fill="none" stroke="#fff" stroke-width="3"/></svg>Extension Kits</li>
    <li><svg viewBox="0 0 36 22"><polyline points="4,4 14,11 4,18" fill="none" stroke="#fff" stroke-width="3"/><polyline points="16,4 26,11 16,18" fill="none" stroke="#fff" stroke-width="3"/></svg>Replacement Caps &amp; Gaskets</li>
  </ul>
  <ul class="product-list right">
    <li><svg viewBox="0 0 36 22"><polyline points="4,4 14,11 4,18" fill="none" stroke="#fff" stroke-width="3"/><polyline points="16,4 26,11 16,18" fill="none" stroke="#fff" stroke-width="3"/></svg>Replacement Nozzles</li>
    <li><svg viewBox="0 0 36 22"><polyline points="4,4 14,11 4,18" fill="none" stroke="#fff" stroke-width="3"/><polyline points="16,4 26,11 16,18" fill="none" stroke="#fff" stroke-width="3"/></svg>Adjustable Hydrant Wrenches</li>
    <li><svg viewBox="0 0 36 22"><polyline points="4,4 14,11 4,18" fill="none" stroke="#fff" stroke-width="3"/><polyline points="16,4 26,11 16,18" fill="none" stroke="#fff" stroke-width="3"/></svg>Hydrant Diffusers</li>
    <li><svg viewBox="0 0 36 22"><polyline points="4,4 14,11 4,18" fill="none" stroke="#fff" stroke-width="3"/><polyline points="16,4 26,11 16,18" fill="none" stroke="#fff" stroke-width="3"/></svg>Hydrant Oil</li>
  </ul>

  <section class="cards">
    <figure class="card"><div class="card-image img-traffic" role="img" aria-label="Hydrant traffic repair kit with breakaway flange and bolts"></div><figcaption class="card-label">Hydrant Traffic Repair Kit Pic</figcaption></figure>
    <figure class="card"><div class="card-image img-extension" role="img" aria-label="Fire hydrant extension kit with barrel and hardware"></div><figcaption class="card-label">Fire Hydrant Extension Kit Pic</figcaption></figure>
    <figure class="card"><div class="card-image img-cap" role="img" aria-label="Red fire hydrant cap with chain"></div><figcaption class="card-label">Fire Hydrant Cap &amp; Chain</figcaption></figure>
    <figure class="card"><div class="card-image img-diffuser" role="img" aria-label="Yellow hydrant diffuser with pressure gauge"></div><figcaption class="card-label">Hydrant Diffuser</figcaption></figure>
    <figure class="card"><div class="card-image img-wrench" role="img" aria-label="Adjustable fire hydrant wrench"></div><figcaption class="card-label">Fire Hydrant Wrench</figcaption></figure>
    <figure class="card"><div class="card-image img-oil" role="img" aria-label="Bottle of hydrant lubricating oil"></div><figcaption class="card-label">Lube Picture</figcaption></figure>
  </section>

  <section class="makers" aria-label="Manufacturers stocked">
    <div class="maker"><span class="maker-mark"></span></div>
    <div class="maker"><span class="maker-mark"></span></div>
    <div class="maker"><span class="maker-mark round"></span></div>
    <div class="maker"><span class="maker-mark round"></span></div>
    <div class="maker"><span class="maker-mark"></span></div>
    <div class="maker"><span class="maker-mark"></span></div>
  </section>

  <div class="contact-call">
    <span class="label">Please Call Us At:</span>
    <svg width="26" height="26" viewBox="0 0 24 24"><path d="M6.6 10.8a15.1 15.1 0 0 0 6.6 6.6l2.2-2.2c.3-.3.7-.4 1-.2 1.1.4 2.3.6 3.6.6.6 0 1 .4 1 1V20c0 .6-.4 1-1 1A17 17 0 0 1 3 4c0-.6.4-1 1-1h3.5c.6 0 1 .4 1 1 0 1.3.2 2.5.6 3.6.1.3 0 .7-.2 1z" fill="#fff"/></svg>
    <span class="number">(800) 555-0142</span>
  </div>
  <div class="contact-web">
    <svg width="28" height="28" viewBox="0 0 24 24" fill="none" stroke="#fff" stroke-width="2"><circle cx="12" cy="12" r="10"/><ellipse cx="12" cy="12" rx="4.5" ry="10"/><line x1="2" y1="12" x2="22" y2="12"/></svg>
    <span>coastalflowline.com</span>
  </div>
</main>
</body>
</html>
```